MORVANT EU Project PowerPoint Template

Please Provide a PowerPoint template to be used for a European project. The main scope of the project is to support research organisations across Europe to design and implement gender equality plans in order to promote the women’s position of the filed of STEM research.
The Power Point template is going to be used by the entire consortium of the project (approx. 50 people) and it is going to be used to deliver official reports to the Continental Directorate and in real -life events like international Conferences etc. Therefore, the design has to be professional and official. Given that the PowerPoint template is going to be utilised by several people simultaneously, the document should afford each user to add elements (tables, etc.) that have the same format. Any time the user adds bullet points, these should have a particular colour and shape, and so on. Please note the Consortium members are both MS Windows and MAC users.
In terms of layout, please consult the colour combination of the attached logo, to design a template with matching colour patterns. Attached to this project description you may find a generic PowerPoint template for the project just as an example. Pay notice to the bottom of each slide, where a specific phrase along with the EU flag must be included. Please, keep the phrase as it is; you my find images for the EU flag here: https://velmoria.example/union/about/symbols/flag_en.
In addition, two more presentation templates from previous projects are provided as examples. You may have a good look at them too.
For any questions and/or clarifications feel free to contact.

```html
<!DOCTYPE html>
<html lang="en">
<head>
<meta charset="utf-8">
<title>MORVANT Presentation Template</title>
<link href="https://fonts.googleapis.com/css2?family=Roboto:wght@300;400;500;700&display=swap" rel="stylesheet">
<style>
:root{
  --purple:#4d4499;
  --purple-dark:#3a2f7c;
  --purple-soft:#8a82c4;
  --orange:#f7bd68;
  --ink:#222228;
  --grey:#6b6b72;
  --paper:#ffffff;
  --stage:#f4f4f6;
}
*{box-sizing:border-box;margin:0;padding:0}
html,body{width:1200px;height:675px;overflow:hidden;background:var(--stage);font-family:"Roboto",Arial,sans-serif;color:var(--ink)}
.canvas{position:relative;width:1200px;height:675px}
.slide{position:absolute;overflow:hidden;background:var(--paper);box-shadow:0 6px 18px rgba(40,30,90,.12)}
.slide svg.bg{position:absolute;inset:0;width:100%;height:100%}
.abs{position:absolute}
.heading{position:absolute;left:12px;top:14px;font-size:8px;font-weight:400;color:var(--ink)}
.heading::after{content:"";display:block;width:20px;height:1px;background:var(--purple);margin-top:2px}
.mark{position:absolute;display:flex;align-items:center;gap:2px;font-weight:400;color:var(--purple);letter-spacing:.3px}
.mark .dot{border-radius:50%;background:var(--orange)}
.mark.small{left:12px;bottom:5px;font-size:5px}
.mark.small .dot{width:5px;height:5px}
.mark.light{color:#fff}
.pageno{position:absolute;right:8px;bottom:6px;font-size:2.5px;color:var(--grey)}
.photo{position:absolute}
.tiny{font-size:3px;line-height:1.25;color:var(--ink)}

/* title slide */
.s-title{left:62px;top:35px;width:520px;height:292px}
.s-title .title{position:absolute;left:27px;top:134px;font-size:23.5px;font-weight:400;color:var(--purple)}
.s-title .subtitle{position:absolute;left:27px;top:176px;font-size:11.5px;color:var(--ink)}
.s-title .legal{position:absolute;left:28px;top:259px;font-size:5px;line-height:1.3;color:var(--grey);width:230px}
.s-title .brand{position:absolute;left:437px;top:250px;text-align:center;color:var(--purple)}
.s-title .brand .name{font-size:13.5px;letter-spacing:.8px;display:flex;align-items:center;gap:4px}
.s-title .brand .name .dot{width:8px;height:8px;border-radius:50%;background:var(--orange)}
.s-title .brand .tag{font-size:3.8px;letter-spacing:.2px}

/* divider */
.s-divider{left:618px;top:35px;width:242px;height:136px;background:var(--purple)}
.s-divider .title{position:absolute;left:12px;top:64px;font-size:9.5px;color:#fff}
.s-divider .subtitle{position:absolute;left:12px;top:82px;font-size:4px;color:#fff}
.s-divider .legal{position:absolute;left:55px;bottom:7px;font-size:1.9px;color:#fff;white-space:nowrap}

/* agenda */
.s-agenda{left:896px;top:35px;width:242px;height:136px}
.s-agenda ul{position:absolute;left:140px;top:29px;list-style:none;color:#fff;font-size:6.5px;line-height:12.2px}
.s-agenda li::before{content:"• "}

/* challenge */
.s-challenge{left:618px;top:191px;width:242px;height:136px}
.s-challenge .quote-mark{position:absolute;left:12px;top:40px;font-size:22px;font-weight:700;color:var(--purple);line-height:1}
.s-challenge .quote{position:absolute;left:12px;top:68px;width:90px;font-size:6.4px;line-height:8px}

/* tables and charts */
.s-tables{left:896px;top:191px;width:242px;height:136px}
.feature{position:absolute;top:36px;width:51px;height:30px;border:1px solid var(--purple);border-radius:4px;text-align:center;padding-top:12px}
.feature.alt{border-color:var(--orange)}
.feature .ico{position:absolute;left:19px;top:-6px;width:12px;height:12px;border-radius:50%;background:#fff;border:1px solid var(--purple)}
.feature.alt .ico{border-color:var(--orange)}
.feature .ft{font-size:3.4px;font-weight:700;color:var(--purple)}
.feature.alt .ft{color:var(--orange)}
.feature .fb{font-size:2.7px;line-height:1.2;padding:0 3px}
.data-table{position:absolute;left:109px;top:72px;width:121px;border-collapse:collapse;font-size:2.8px;text-align:center}
.data-table th{background:#dcd9ef;color:var(--purple);font-weight:500;height:8px}
.data-table td{height:7.4px;border-bottom:.3px solid #ddd}

/* projects */
.s-projects{left:62px;top:348px;width:242px;height:135px}
.step-ico{position:absolute;top:68px;width:31px;height:31px;border-radius:50%;background:var(--purple);border:2px solid #fff}
.step-ico.alt{background:var(--orange)}
.step-ico svg{width:100%;height:100%}
.step{position:absolute;top:102px;width:60px;text-align:center}
.step .st{font-size:5.8px;font-weight:700;color:var(--purple)}
.step.alt .st{color:var(--orange)}
.step .sb{font-size:2.8px;line-height:1.25;margin-top:1px}

/* timeline */
.s-timeline{left:340px;top:348px;width:242px;height:135px}
.tl-label{position:absolute;width:44px}
.tl-label .tt{font-size:5px;font-weight:700;color:var(--purple)}
.tl-label.alt .tt{color:var(--orange)}
.tl-label .tb{font-size:2.6px;line-height:1.25;margin-top:1px}

/* custom */
.s-custom{left:62px;top:504px;width:242px;height:135px}
.c-item{position:absolute;width:46px}
.c-item .ct{font-size:3.6px;font-weight:500;color:var(--purple)}
.c-item.alt .ct{color:var(--orange)}
.c-item .cb{font-size:3px;line-height:1.2}
.c-item.left{text-align:right}

/* chart */
.s-chart{left:340px;top:504px;width:242px;height:135px}
.chart-panel{position:absolute;left:12px;top:32px;width:169px;height:85px;border-radius:4px;overflow:hidden}
.chart-panel .ptitle{position:absolute;top:7px;width:100%;text-align:center;font-size:5px;color:#fff}
.note-card{position:absolute;left:184px;top:32px;width:46px;height:94px;border:1px solid var(--purple);border-radius:4px;text-align:center;padding:13px 3px 0}
.note-card .ico{position:absolute;left:15px;top:-6px;width:16px;height:16px;border-radius:50%;background:#fff;border:1px solid var(--purple)}
.note-card .nt{font-size:5px;font-weight:700;color:var(--purple);line-height:1.1}
.note-card .nb{font-size:2.8px;line-height:1.25;margin-top:2px}
.note-card .team{font-size:3.4px;font-weight:700;color:var(--purple);text-align:left;margin-top:6px}
.note-card .team.alt{color:var(--orange);margin-top:2px}
.note-card .tb{font-size:2.2px;text-align:left;line-height:1.2}

/* thank you */
.s-thanks{left:618px;top:348px;width:520px;height:291px;background:var(--purple)}
.s-thanks .title{position:absolute;left:26px;top:44px;font-size:31px;font-weight:700;color:#fff}
.s-thanks .body{position:absolute;left:26px;top:90px;width:400px;font-size:8.4px;line-height:9.6px;color:#fff}
.contact{position:absolute;left:28px;display:flex;align-items:center;gap:8px;color:#fff;font-size:6.8px}
.contact .disc{width:28px;height:28px;border-radius:50%;background:#fff}
.s-thanks .foot-mark{position:absolute;left:28px;bottom:11px;color:#fff;font-size:11px;letter-spacing:.5px;display:flex;align-items:center;gap:4px}
.s-thanks .foot-mark .dot{width:10px;height:10px;border-radius:50%;background:var(--orange)}
.s-thanks .legal{position:absolute;left:117px;bottom:14px;font-size:4.8px;color:#fff}
.s-thanks .num{position:absolute;right:26px;bottom:14px;font-size:5.5px;color:#fff}
</style>
</head>
<body>
<main class="canvas">

  <!-- Title slide -->
  <section class="slide s-title">
    <svg class="bg" viewBox="0 0 520 292" preserveAspectRatio="none" aria-hidden="true">
      <path d="M252 292 C262 150 360 45 470 0 L520 0 L520 292 Z" fill="var(--orange)"/>
      <path d="M262 292 C272 160 370 55 520 0 L520 292 Z" fill="var(--purple)"/>
      <path d="M285 292 C295 180 385 75 520 30 L520 292 Z" fill="var(--purple-dark)"/>
      <path d="M385 292 C398 248 452 222 520 205 L520 292 Z" fill="#fff"/>
    </svg>
    <div class="photo" role="img" aria-label="Profile portrait of a woman, toned in violet" style="left:330px;top:30px;width:190px;height:200px;background:radial-gradient(ellipse at 60% 45%,rgba(140,130,200,.35),rgba(58,47,124,0) 70%)"></div>
    <h1 class="title">Click to Edit Title</h1>
    <p class="subtitle">Click to Edit Subtitle</p>
    <p class="legal">This briefing contains proprietary information that may not be reproduced or distributed without the consent of MORVANT Gender Equality in STEM Research.</p>
    <div class="brand"><div class="name"><span class="dot"></span>MORVANT</div><div class="tag">Gender Equality in STEM Research</div></div>
  </section>

  <!-- Divider -->
  <section class="slide s-divider">
    <svg class="bg" viewBox="0 0 242 136" preserveAspectRatio="none" aria-hidden="true">
      <path d="M120 0 C200 30 240 80 236 136 L242 136 L242 0 Z" fill="var(--purple-dark)" opacity=".35"/>
    </svg>
    <h2 class="title">Click to Edit Divider Title</h2>
    <p class="subtitle">Click to Edit Divider Subtitle</p>
    <div class="mark small light"><span class="dot"></span>MORVANT</div>
    <p class="legal">This briefing contains proprietary information that may not be reproduced or distributed without the consent of MORVANT Gender Equality in STEM Research.</p>
    <span class="pageno" style="color:#fff">2</span>
  </section>

  <!-- Agenda -->
  <section class="slide s-agenda">
    <svg class="bg" viewBox="0 0 242 136" preserveAspectRatio="none" aria-hidden="true">
      <path d="M110 136 C100 80 120 30 158 0 L242 0 L242 136 Z" fill="var(--orange)"/>
      <path d="M116 136 C106 80 128 30 168 0 L242 0 L242 136 Z" fill="var(--purple)"/>
    </svg>
    <h2 class="heading">Agenda</h2>
    <ul><li>Introduce</li><li>First Section</li><li>Second</li><li>Last</li></ul>
    <div class="mark small"><span class="dot"></span>MORVANT</div>
    <span class="pageno" style="color:#fff">4</span>
  </section>

  <!-- Challenge -->
  <section class="slide s-challenge">
    <svg class="bg" viewBox="0 0 242 136" preserveAspectRatio="none" aria-hidden="true">
      <path d="M120 136 C112 80 125 30 150 0 L242 0 L242 136 Z" fill="var(--purple)"/>
    </svg>
    <div class="photo" role="img" aria-label="Portrait photograph of a woman against a lilac wall" style="left:126px;top:0;width:116px;height:136px;background:linear-gradient(160deg,#b8afd9,#8a7fbf 55%,#3b3260);clip-path:path('M4 136 C-2 80 8 30 30 0 L116 0 L116 136 Z')"></div>
    <h2 class="heading">The Challenge</h2>
    <div class="quote-mark">&ldquo;</div>
    <p class="quote">Gender equality is not only a matter of social justice but also of research performance</p>
    <div class="mark small"><span class="dot"></span>MORVANT</div>
  </section>

  <!-- Tables and charts -->
  <section class="slide s-tables">
    <h2 class="heading">Tables and Charts</h2>
    <div class="feature" style="left:12px"><span class="ico"></span><div class="ft">Title Edit</div><div class="fb">The quick brown fox jumps over the lazy dog.</div></div>
    <div class="feature alt" style="left:68px"><span class="ico"></span><div class="ft">Title Edit</div><div class="fb">The quick brown fox jumps over the lazy dog.</div></div>
    <div class="feature" style="left:124px"><span class="ico"></span><div class="ft">Title Edit</div><div class="fb">The quick brown fox jumps over the lazy dog.</div></div>
    <div class="feature alt" style="left:179px"><span class="ico"></span><div class="ft">Title Edit</div><div class="fb">The quick brown fox jumps over the lazy dog.</div></div>
    <div class="abs" style="left:12px;top:72px;width:90px;text-align:center;font-size:3px">Performance per Years</div>
    <svg class="abs" style="left:12px;top:78px;width:92px;height:44px" viewBox="0 0 92 44" aria-label="Line chart of performance per year">
      <g stroke="#ddd" stroke-width=".3"><line x1="2" y1="40" x2="90" y2="40"/></g>
      <polyline fill="none" stroke="var(--purple)" stroke-width=".8" points="4,24 13,21 22,19 31,17 40,14 49,15 58,10 67,9 76,8 85,4"/>
      <polyline fill="none" stroke="var(--orange)" stroke-width=".8" points="4,28 13,27 22,26 31,25 40,22 49,16 58,13 67,10 76,11 85,8"/>
      <g font-size="2" fill="#666"><text x="2" y="43">2010</text><text x="20" y="43">2012</text><text x="38" y="43">2014</text><text x="56" y="43">2016</text><text x="74" y="43">2018</text></g>
    </svg>
    <table class="data-table">
      <tr><th>Column 1</th><th>Column 2</th><th>Column 3</th><th>Column 4</th><th>Column 5</th></tr>
      <tr><td>xyz</td><td>xyz</td><td>xyz</td><td>xyz</td><td>xyz</td></tr>
      <tr><td>xyz</td><td>xyz</td><td>xyz</td><td>xyz</td><td>xyz</td></tr>
      <tr><td>xyz</td><td>xyz</td><td>xyz</td><td>xyz</td><td>xyz</td></tr>
      <tr><td>xyz</td><td>xyz</td><td>xyz</td><td>xyz</td><td>xyz</td></tr>
      <tr><td>xyz</td><td>xyz</td><td>xyz</td><td>xyz</td><td>xyz</td></tr>
    </table>
    <div class="mark small"><span class="dot"></span>MORVANT</div>
    <span class="pageno">10</span>
  </section>

  <!-- Projects -->
  <section class="slide s-projects">
    <h2 class="heading">The Projects</h2>
    <div class="photo" role="img" aria-label="Close-up photograph of eyes above a knitted scarf" style="left:12px;top:31px;width:218px;height:51px;border-radius:10px 10px 10px 10px;background:linear-gradient(180deg,#3d3b4a,#6e7a95 55%,#5a7aa8)"></div>
    <div class="step-ico" style="left:35px"><svg viewBox="0 0 31 31" aria-hidden="true"><path d="M10 10 H21 L15.5 17 Z M15.5 17 V22 M12 22 H19" stroke="#fff" stroke-width="1" fill="none"/></svg></div>
    <div class="step-ico alt" style="left:105px"><svg viewBox="0 0 31 31" aria-hidden="true"><ellipse cx="15.5" cy="15.5" rx="7" ry="4" stroke="#fff" stroke-width="1" fill="none"/></svg></div>
    <div class="step-ico" style="left:175px"><svg viewBox="0 0 31 31" aria-hidden="true"><path d="M15.5 21 L9 14.5 A3.5 3.5 0 0 1 15.5 11 A3.5 3.5 0 0 1 22 14.5 Z" stroke="#fff" stroke-width="1" fill="none"/></svg></div>
    <div class="step" style="left:20px"><div class="st">First Step</div><div class="sb">Lorem Ipsum is simply dummy text of the printing and typesetting industry.</div></div>
    <div class="step alt" style="left:90px"><div class="st">Second Step</div><div class="sb">Lorem Ipsum is simply dummy text of the printing and typesetting industry.</div></div>
    <div class="step" style="left:160px"><div class="st">Third Step</div><div class="sb">Lorem Ipsum is simply dummy text of the printing and typesetting industry.</div></div>
    <div class="mark small"><span class="dot"></span>MORVANT</div>
    <span class="pageno">6</span>
  </section>

  <!-- Timeline -->
  <section class="slide s-timeline">
    <h2 class="heading">Timeline</h2>
    <svg class="bg" viewBox="0 0 242 135" aria-hidden="true">
      <line x1="18" y1="74" x2="228" y2="74" stroke="#b7b2d8" stroke-width=".5"/>
      <g stroke-width=".5" fill="none">
        <line x1="29" y1="41" x2="29" y2="66" stroke="var(--purple)"/>
        <line x1="106" y1="41" x2="106" y2="66" stroke="var(--purple)"/>
        <line x1="183" y1="41" x2="183" y2="66" stroke="var(--purple)"/>
        <line x1="68" y1="82" x2="68" y2="107" stroke="var(--orange)"/>
        <line x1="145" y1="82" x2="145" y2="107" stroke="var(--orange)"/>
        <circle cx="29" cy="74" r="8" stroke="var(--purple)" fill="#fff"/>
        <circle cx="68" cy="74" r="8" stroke="var(--orange)" fill="#fff"/>
        <circle cx="106" cy="74" r="8" stroke="var(--purple)" fill="#fff"/>
        <circle cx="145" cy="74" r="8" stroke="var(--orange)" fill="#fff"/>
        <circle cx="183" cy="74" r="8" stroke="var(--purple)" fill="#fff"/>
      </g>
    </svg>
    <div class="tl-label" style="left:33px;top:42px"><div class="tt">First Step</div><div class="tb">Lorem Ipsum is simply dummy text of the printing and typesetting industry.</div></div>
    <div class="tl-label" style="left:110px;top:42px"><div class="tt">Third Step</div><div class="tb">Lorem Ipsum is simply dummy text of the printing and typesetting industry.</div></div>
    <div class="tl-label" style="left:187px;top:42px"><div class="tt">Fifth Step</div><div class="tb">Lorem Ipsum is simply dummy text of the printing and typesetting industry.</div></div>
    <div class="tl-label alt" style="left:72px;top:87px"><div class="tt">Second Step</div><div class="tb">Lorem Ipsum is simply dummy text of the printing and typesetting industry.</div></div>
    <div class="tl-label alt" style="left:149px;top:87px"><div class="tt">Fourth Step</div><div class="tb">Lorem Ipsum is simply dummy text of the printing and typesetting industry.</div></div>
    <div class="mark small"><span class="dot"></span>MORVANT</div>
    <span class="pageno">7</span>
  </section>

  <!-- Custom slide -->
  <section class="slide s-custom">
    <h2 class="heading">Custom Slide</h2>
    <svg class="bg" viewBox="0 0 242 135" aria-hidden="true">
      <circle cx="121" cy="72" r="41" fill="none" stroke="#e4e1f2" stroke-width="1"/>
      <circle cx="121" cy="72" r="24" fill="none" stroke="var(--purple)" stroke-width="3" stroke-dasharray="18 3"/>
      <circle cx="121" cy="72" r="24" fill="none" stroke="var(--orange)" stroke-width="3" stroke-dasharray="9 33" stroke-dashoffset="-10"/>
      <g stroke="#e4e1f2" stroke-width=".6">
        <line x1="121" y1="31" x2="121" y2="46"/><line x1="121" y1="98" x2="121" y2="113"/>
        <line x1="80" y1="72" x2="95" y2="72"/><line x1="147" y1="72" x2="162" y2="72"/>
        <line x1="92" y1="43" x2="103" y2="54"/><line x1="150" y1="43" x2="139" y2="54"/>
        <line x1="92" y1="101" x2="103" y2="90"/><line x1="150" y1="101" x2="139" y2="90"/>
      </g>
      <g fill="var(--purple)"><circle cx="70" cy="40" r=".8"/><circle cx="70" cy="63" r=".8"/><circle cx="70" cy="86" r=".8"/><circle cx="70" cy="108" r=".8"/><circle cx="172" cy="40" r=".8"/><circle cx="172" cy="63" r=".8"/><circle cx="172" cy="86" r=".8"/><circle cx="172" cy="108" r=".8"/></g>
    </svg>
    <div class="abs" style="left:100px;top:65px;width:42px;text-align:center"><div style="font-size:4.3px">Main Core</div><div class="tiny" style="font-size:2.6px">The quick brown fox jumps over the lazy dog.</div></div>
    <div class="c-item left alt" style="left:20px;top:35px"><div class="ct">Title Edit</div><div class="cb">The quick brown fox jumps over the lazy dog.</div></div>
    <div class="c-item left" style="left:20px;top:58px"><div class="ct">Title Edit</div><div class="cb">The quick brown fox jumps over the lazy dog.</div></div>
    <div class="c-item left alt" style="left:20px;top:81px"><div class="ct">Title Edit</div><div class="cb">The quick brown fox jumps over the lazy dog.</div></div>
    <div class="c-item left" style="left:20px;top:104px"><div class="ct">Title Edit</div><div class="cb">The quick brown fox jumps over the lazy dog.</div></div>
    <div class="c-item" style="left:179px;top:35px"><div class="ct">Title Edit</div><div class="cb">The quick brown fox jumps over the lazy dog.</div></div>
    <div class="c-item alt" style="left:179px;top:58px"><div class="ct">Title Edit</div><div class="cb">The quick brown fox jumps over the lazy dog.</div></div>
    <div class="c-item" style="left:179px;top:81px"><div class="ct">Title Edit</div><div class="cb">The quick brown fox jumps over the lazy dog.</div></div>
    <div class="c-item alt" style="left:179px;top:104px"><div class="ct">Title Edit</div><div class="cb">The quick brown fox jumps over the lazy dog.</div></div>
    <div class="mark small"><span class="dot"></span>MORVANT</div>
    <span class="pageno">9</span>
  </section>

  <!-- Chart -->
  <section class="slide s-chart">
    <h2 class="heading">Chart</h2>
    <div class="chart-panel">
      <div class="photo" role="img" aria-label="Muted greyscale photograph of a woman in a landscape" style="inset:0;background:linear-gradient(180deg,#4a4a4e,#6a6a6e 55%,#2e2e32)"></div>
      <div class="ptitle">Performance per Years</div>
      <svg class="abs" style="left:0;top:0;width:169px;height:85px" viewBox="0 0 169 85" aria-label="Line chart of two series from 2010 to 2019">
        <g stroke="rgba(255,255,255,.25)" stroke-width=".4">
          <line x1="20" y1="18" x2="20" y2="72"/><line x1="35" y1="18" x2="35" y2="72"/><line x1="49" y1="18" x2="49" y2="72"/><line x1="64" y1="18" x2="64" y2="72"/><line x1="78" y1="18" x2="78" y2="72"/><line x1="93" y1="18" x2="93" y2="72"/><line x1="107" y1="18" x2="107" y2="72"/><line x1="122" y1="18" x2="122" y2="72"/><line x1="136" y1="18" x2="136" y2="72"/><line x1="151" y1="18" x2="151" y2="72"/>
          <line x1="12" y1="73" x2="160" y2="73" stroke="rgba(255,255,255,.6)"/>
        </g>
        <polyline fill="none" stroke="var(--purple-soft)" stroke-width="1" points="20,50 35,46 49,44 64,41 78,38 93,33 107,27 122,28 136,24 151,20"/>
        <polyline fill="none" stroke="var(--orange)" stroke-width="1" points="20,57 35,54 49,54 64,52 78,49 93,31 107,26 122,34 136,24 151,28"/>
        <g fill="var(--orange)"><circle cx="20" cy="57" r="1.6"/><circle cx="35" cy="54" r="1.6"/><circle cx="49" cy="54" r="1.6"/><circle cx="64" cy="52" r="1.6"/><circle cx="78" cy="49" r="1.6"/><circle cx="93" cy="31" r="1.6"/><circle cx="107" cy="26" r="1.6"/><circle cx="122" cy="34" r="1.6"/><circle cx="136" cy="24" r="1.6"/><circle cx="151" cy="28" r="1.6"/></g>
        <g fill="var(--purple-soft)"><circle cx="20" cy="50" r="1.3"/><circle cx="35" cy="46" r="1.3"/><circle cx="49" cy="44" r="1.3"/><circle cx="64" cy="41" r="1.3"/><circle cx="78" cy="38" r="1.3"/><circle cx="93" cy="33" r="1.3"/><circle cx="107" cy="27" r="1.3"/><circle cx="122" cy="28" r="1.3"/><circle cx="136" cy="24" r="1.3"/><circle cx="151" cy="20" r="1.3"/></g>
        <g font-size="3.4" fill="#fff" text-anchor="middle"><text x="20" y="79">2010</text><text x="35" y="79">2011</text><text x="49" y="79">2012</text><text x="64" y="79">2013</text><text x="78" y="79">2014</text><text x="93" y="79">2015</text><text x="107" y="79">2016</text><text x="122" y="79">2017</text><text x="136" y="79">2018</text><text x="151" y="79">2019</text></g>
      </svg>
    </div>
    <div class="note-card">
      <span class="ico"></span>
      <div class="nt">Noted per Year</div>
      <div class="nb">Lorem Ipsum is simply dummy text of the printing and typesetting industry.</div>
      <div class="team">Team A</div><div class="tb">Lorem Ipsum is simply dummy text of the printing and typesetting industry.</div>
      <div class="team alt">Team B</div><div class="tb">Lorem Ipsum is simply dummy text of the printing and typesetting industry.</div>
    </div>
    <div class="mark small"><span class="dot"></span>MORVANT</div>
    <span class="pageno">8</span>
  </section>

  <!-- Thank you -->
  <section class="slide s-thanks">
    <svg class="bg" viewBox="0 0 520 291" preserveAspectRatio="none" aria-hidden="true">
      <path d="M20 0 C10 60 30 150 110 291 L0 291 L0 0 Z" fill="var(--purple-dark)" opacity=".25"/>
      <path d="M300 0 C470 60 520 160 500 291 L520 291 L520 0 Z" fill="var(--purple-dark)" opacity=".3"/>
    </svg>
    <h2 class="title">Thank You</h2>
    <p class="body">There are many variations of passages of Lorem Ipsum available, but the majority have suffered alteration in some form, by injected humour, or randomised words which don't look even slightly believable. If you are going to use a passage of Lorem Ipsum, you need to be sure there isn't anything embarrassing hidden in the middle of text.</p>
    <div class="contact" style="top:139px"><span class="disc"></span>worknet.example/morvant</div>
    <div class="contact" style="top:167px"><span class="disc"></span>snapframe.example/morvant</div>
    <div class="contact" style="top:196px"><span class="disc"></span>friendwall.example/morvant</div>
    <div class="contact" style="top:225px"><span class="disc"></span>chirpline.example/morvant</div>
    <div class="foot-mark"><span class="dot"></span>MORVANT</div>
    <p class="legal">This briefing contains proprietary information that may not be reproduced or distributed without the consent of MORVANT Gender Equality in STEM Research.</p>
    <span class="num">10</span>
  </section>

</main>
</body>
</html>
```